The Timber Loft

We need a business card design for our wardrobe company.
Please visit our website www.zorvelcabinets.com to get an idea of who we are.

```html
<!DOCTYPE html>
<html lang="en">
<head>
<meta charset="utf-8">
<title>The Timber Loft – Business Card</title>
<link href="https://fonts.googleapis.com/css2?family=Montserrat:wght@400;500;600;700&display=swap" rel="stylesheet">
<style>
  :root {
    --backdrop: #2a2a2a;
    --card-dark: #141414;
    --card-light: #ffffff;
    --ink-light: #ffffff;
    --ink-dark: #111111;
    --ink-muted: #3c3c3c;
    --divider: #555555;
  }
  * { margin: 0; padding: 0; box-sizing: border-box; }
  html, body {
    width: 1200px; height: 895px; overflow: hidden;
    background: var(--backdrop);
    font-family: "Montserrat", Arial, sans-serif;
  }
  .canvas { position: relative; width: 1200px; height: 895px; }
  .card {
    position: absolute; left: 310px; width: 580px; height: 331px;
    box-shadow: 0 10px 30px rgba(0,0,0,0.55);
  }
  .card--front { top: 64px; background: var(--card-dark); color: var(--ink-light); }
  .card--back { top: 500px; background: var(--card-light); color: var(--ink-dark); }

  .brand { position: absolute; display: flex; align-items: center; gap: 14px; }
  .brand__mark { width: 22px; height: 22px; border: 2px solid currentColor; flex: none; }
  .brand__name { font-weight: 600; font-size: 17px; letter-spacing: 0.4px; text-transform: uppercase; white-space: nowrap; }
  .brand__tagline { font-weight: 600; font-size: 14px; margin-top: 4px; white-space: nowrap; }

  .card--front .brand { left: 150px; top: 140px; }
  .card--back .brand { left: 34px; top: 140px; }
  .card--back .brand__name { font-size: 14px; }
  .card--back .brand__tagline { font-size: 12px; }

  .divider {
    position: absolute; left: 316px; top: 78px; width: 1px; height: 178px;
    background: var(--divider);
  }
  .contact { position: absolute; left: 336px; top: 78px; }
  .contact__name { font-weight: 700; font-size: 17px; letter-spacing: 0.5px; text-transform: uppercase; }
  .contact__role { font-size: 11px; font-weight: 500; margin-top: 3px; color: var(--ink-muted); }
  .contact__address { font-size: 12.5px; line-height: 20px; margin-top: 14px; color: var(--ink-muted); }
  .contact__list { list-style: none; margin-top: 4px; }
  .contact__item {
    display: flex; align-items: center; gap: 9px;
    font-size: 12.5px; line-height: 22px; color: var(--ink-muted);
  }
  .contact__icon { width: 12px; height: 12px; fill: var(--ink-dark); flex: none; }
</style>
</head>
<body>
<div class="canvas">

  <section class="card card--front">
    <div class="brand">
      <span class="brand__mark"></span>
      <div>
        <div class="brand__name">The Timber Loft</div>
        <div class="brand__tagline">Built to Fit Every Room</div>
      </div>
    </div>
  </section>

  <section class="card card--back">
    <div class="brand">
      <span class="brand__mark"></span>
      <div>
        <div class="brand__name">The Timber Loft</div>
        <div class="brand__tagline">Built to Fit Every Room</div>
      </div>
    </div>

    <div class="divider"></div>

    <div class="contact">
      <div class="contact__name">Marcus Hale</div>
      <div class="contact__role">Owner</div>
      <div class="contact__address">Unit 4, 27 Alder Street<br>Leeds LS2 7QH</div>
      <ul class="contact__list">
        <li class="contact__item">
          <svg class="contact__icon" viewBox="0 0 24 24"><path d="M6.6 10.8a15.2 15.2 0 0 0 6.6 6.6l2.2-2.2a1 1 0 0 1 1-.25 11.4 11.4 0 0 0 3.6.57 1 1 0 0 1 1 1V20a1 1 0 0 1-1 1A17 17 0 0 1 3 4a1 1 0 0 1 1-1h3.5a1 1 0 0 1 1 1c0 1.25.2 2.45.57 3.57a1 1 0 0 1-.25 1z"/></svg>
          0113 496 0718
        </li>
        <li class="contact__item">
          <svg class="contact__icon" viewBox="0 0 24 24"><path d="M2 4h20v3l-10 7L2 7z"/><path d="M2 9l10 7 10-7v11H2z"/></svg>
          info@zorvelcabinets.com
        </li>
        <li class="contact__item">
          <svg class="contact__icon" viewBox="0 0 24 24"><circle cx="12" cy="12" r="10"/><path d="M2 12h20M12 2c3 3 3 17 0 20M12 2c-3 3-3 17 0 20" stroke="#fff" stroke-width="1.4" fill="none"/></svg>
          www.zorvelcabinets.com
        </li>
      </ul>
    </div>
  </section>

</div>
</body>
</html>
```